Orthodontist Needs Promotional Discount Postcard

5.5 x 8.5 Horizontal 2-Sided Postcard for mailing.
Images & Logo on both sides okay; must be free stock Images from legit sources only, or use attached images. See our website for information, ShoreLaneSmiles.com
Context to include:
New Patient Special $500 off Braces or Clear Aligners
Cannot be combined with any other discounts.
Major dental insurance plans and Cara-Plan accepted
Affordable payment options are available
Call to schedule your free consultation
Present this new patient offer to receive your discount.
Offer ends January 31, 2022.
805-472-9186 www. ShoreLaneSmiles.com
462 N. Harlow Street, Suite B, Ventura, CA 93001-2718
office@shorelanesmiles.com

```html
<!DOCTYPE html>
<html lang="en">
<head>
<meta charset="utf-8">
<title>Shore Lane Smiles – New Patient Postcard</title>
<link rel="stylesheet" href="https://fonts.googleapis.com/css2?family=Poppins:wght@500;600;700;800&family=Oswald:wght@500;600&display=swap">
<style>
:root{
  --page:#f2f0ec;
  --blue:#1e8fcf;
  --blue-dark:#146ea6;
  --blue-light:#36b0e6;
  --grey:#6b6c70;
  --grey-dark:#57585c;
  --red:#e0231b;
  --white:#ffffff;
  --ink:#2b2b2e;
}
*{box-sizing:border-box;margin:0;padding:0}
html,body{width:1200px;height:2297px;overflow:hidden;background:var(--page)}
body{position:relative;font-family:"Poppins",sans-serif;color:var(--ink)}
.postcard{position:absolute;left:204px;width:775px;height:501px;background:var(--white);overflow:hidden;box-shadow:0 3px 10px rgba(0,0,0,.18)}
.postcard--front{top:1049px}
.postcard--back{top:1624px}
.card-art{position:absolute;inset:0}
.abs{position:absolute}
.brand{display:flex;align-items:center;gap:8px}
.brand-dot{width:40px;height:40px;border-radius:50%;background:var(--blue);flex:none}
.brand-name{font-family:"Poppins",sans-serif;font-weight:600;font-size:19px;color:var(--blue);letter-spacing:.5px;white-space:nowrap}
.brand--back{left:469px;top:49px;gap:7px}
.brand--back .brand-dot{width:34px;height:34px}
.brand--back .brand-name{font-size:14px;letter-spacing:.3px}
.headline{left:38px;top:88px;font-weight:800;font-size:46px;line-height:1;color:var(--blue-dark);letter-spacing:-.5px}
.special{left:39px;top:150px;width:322px;height:51px;display:flex;border:2px solid var(--grey);border-radius:8px;overflow:hidden;background:var(--white)}
.special-label{width:147px;background:var(--grey);color:var(--white);font-weight:800;font-size:28px;display:flex;align-items:center;justify-content:center}
.special-amount{flex:1;display:flex;align-items:center;justify-content:center;font-family:"Oswald",sans-serif;font-weight:600;font-size:42px;color:var(--red);gap:8px}
.special-amount sup{font-size:18px;align-self:flex-start;margin-top:4px;margin-right:-6px}
.special-amount .off{color:var(--ink)}
.subline{left:39px;font-weight:800;font-size:21px;line-height:1.2;white-space:nowrap}
.subline--grey{top:212px;color:var(--grey)}
.subline--blue{top:244px;color:var(--blue-dark)}
.offer-box{display:flex;border-radius:7px;overflow:hidden;background:var(--white)}
.offer-text{display:flex;flex-direction:column;justify-content:center;padding-left:8px;color:var(--grey);font-weight:700;line-height:1.15;white-space:nowrap}
.offer-cta{background:var(--red);color:var(--white);font-family:"Oswald",sans-serif;font-weight:600;display:flex;flex-direction:column;align-items:center;justify-content:center;line-height:.95}
.front-offer{left:39px;top:363px;width:345px;height:71px}
.front-offer .offer-text{width:216px}
.front-offer .l1{font-size:14px}
.front-offer .l2{font-size:21px}
.front-offer .offer-cta{flex:1;font-size:29px}
.front-ends{left:396px;top:370px;color:var(--white);font-weight:800;font-size:29px;line-height:1.05}
.front-year{left:597px;top:354px;color:var(--white);font-family:"Oswald",sans-serif;font-weight:600;font-size:74px;line-height:1}
.footer{left:0;right:0;display:flex;align-items:center;color:var(--white);font-weight:600}
.front-footer{top:449px;height:52px}
.contact-phone{display:flex;align-items:center;gap:8px}
.icon{width:16px;height:16px;flex:none}
.phone-num{font-weight:700;line-height:1}
.email{font-size:11px;font-weight:600;line-height:1.2}
.front-footer .phone-block{position:absolute;left:40px;top:6px;color:var(--ink)}
.front-footer .phone-num{font-size:22px}
.front-footer .addr{position:absolute;left:280px;top:7px;display:flex;gap:6px;font-size:14.5px;line-height:1.25}
.front-footer .web{position:absolute;left:495px;top:12px;display:flex;gap:10px;font-size:14.5px;align-items:center}
.features{left:28px;top:232px;width:400px;display:flex}
.feature{flex:1;display:flex;flex-direction:column;align-items:flex-start;padding-left:14px;color:var(--white);font-weight:600;font-size:13.5px;line-height:1.25}
.feature + .feature{border-left:1px dashed rgba(255,255,255,.55)}
.feature-icon{width:36px;height:36px;margin-bottom:6px}
.back-offer{left:39px;top:352px;width:253px;height:48px}
.back-offer .offer-text{width:160px;padding-left:10px}
.back-offer .l1{font-size:12.5px;font-family:"Oswald",sans-serif;font-weight:500}
.back-offer .l2{font-size:20px;font-family:"Oswald",sans-serif;font-weight:500}
.back-offer .offer-cta{flex:1;font-size:22px}
.back-ends{left:300px;top:354px;color:var(--white);font-weight:600;font-size:16px;line-height:1.2}
.back-rule{left:39px;top:419px;width:340px;height:1px;background:rgba(255,255,255,.4)}
.back-footer{left:39px;top:429px;color:var(--white);font-size:8px;font-weight:600}
.back-footer .row{display:flex;align-items:center;gap:6px;white-space:nowrap}
.back-footer .phone-num{font-size:16px;font-weight:600}
.back-footer .col2{position:absolute;left:135px;top:3px;display:flex;flex-direction:column;gap:4px}
.stamp{left:678px;top:39px;width:57px;height:56px;background:#bdbdbd}
.address-line{left:503px;width:232px;height:1px;background:#555}
</style>
</head>
<body>

<section class="postcard postcard--front" aria-label="Postcard front">
  <svg class="card-art" viewBox="0 0 775 501" width="775" height="501">
    <defs>
      <linearGradient id="bandBlue" x1="0" y1="0" x2="1" y2="1">
        <stop offset="0" stop-color="#1a7fbf"/>
        <stop offset=".55" stop-color="#39aee4"/>
        <stop offset="1" stop-color="#1a78b5"/>
      </linearGradient>
      <radialGradient id="smileTone" cx=".5" cy=".5" r=".6">
        <stop offset="0" stop-color="#f7eeec"/>
        <stop offset=".6" stop-color="#efc3bd"/>
        <stop offset="1" stop-color="#e3a49d"/>
      </radialGradient>
    </defs>
    <path d="M0 330 Q330 360 775 215 L775 449 L0 449 Z" fill="url(#bandBlue)"/>
    <path d="M0 303 Q330 330 430 295 L470 282 L470 294 Q330 350 0 322 Z" fill="#6b6c70"/>
    <circle cx="580" cy="163" r="207" fill="#36b0e6"/>
    <circle cx="580" cy="163" r="200" fill="#ffffff"/>
    <circle cx="582" cy="160" r="194" fill="url(#smileTone)" role="img" aria-label="Photo of a bright, white-toothed smile with a dental mirror"/>
    <circle cx="709" cy="283" r="76" fill="#ffffff"/>
    <circle cx="709" cy="283" r="70" fill="#e6c6c2" role="img" aria-label="Close-up photo of teeth with metal braces"/>
    <path d="M0 449 H775 V501 H0 Z" fill="#6b6c70"/>
    <path d="M0 449 H245 Q262 470 268 501 H0 Z" fill="#ffffff"/>
    <path d="M245 449 L252 449 Q270 470 276 501 L268 501 Q262 470 245 449 Z" fill="#2b2b2e"/>
  </svg>

  <div class="abs brand" style="left:38px;top:29px">
    <span class="brand-dot"></span><span class="brand-name">SHORE LANE SMILES</span>
  </div>
  <h1 class="abs headline">NEW PATIENT</h1>
  <div class="abs special">
    <span class="special-label">SPECIAL</span>
    <span class="special-amount"><sup>$</sup>500 <span class="off">OFF</span></span>
  </div>
  <p class="abs subline subline--grey">BRACES OR CLEAR ALIGNERS</p>
  <p class="abs subline subline--blue">CANNOT BE COMBINED WITH<br>ANY OTHER DISCOUNTS.</p>

  <div class="abs offer-box front-offer">
    <div class="offer-text"><span class="l1">PRESENT THIS NEW PATIENT</span><span class="l2">OFFER TO RECEIVE</span></div>
    <div class="offer-cta"><span>YOUR</span><span>DISCOUNT</span></div>
  </div>
  <p class="abs front-ends">OFFER ENDS<br>JANUARY 31,</p>
  <p class="abs front-year">2022</p>

  <div class="abs footer front-footer">
    <div class="phone-block">
      <div class="contact-phone">
        <svg class="icon" viewBox="0 0 16 16"><path d="M4 1l3 3-1.6 1.6a9 9 0 0 0 5 5L12 9l3 3-2 2C7 14 2 9 2 3z" fill="#1e8fcf"/></svg>
        <span class="phone-num">805-472-9186</span>
      </div>
      <div class="contact-phone">
        <svg class="icon" viewBox="0 0 16 16"><circle cx="8" cy="8" r="7" fill="#1e8fcf"/><rect x="4" y="5.5" width="8" height="5" fill="none" stroke="#fff"/></svg>
        <span class="email">office@shorelanesmiles.com</span>
      </div>
    </div>
    <div class="addr">
      <svg class="icon" viewBox="0 0 16 16"><path d="M8 1a5 5 0 0 1 5 5c0 4-5 9-5 9S3 10 3 6a5 5 0 0 1 5-5z" fill="#fff"/><circle cx="8" cy="6" r="2" fill="#6b6c70"/></svg>
      <span>Harlow Street, Suite B,<br>Ventura, CA 93001-2718</span>
    </div>
    <div class="web">
      <svg class="icon" viewBox="0 0 16 16"><circle cx="8" cy="8" r="7" fill="none" stroke="#fff" stroke-width="1.3"/><path d="M1 8h14M8 1c-3 3-3 11 0 14M8 1c3 3 3 11 0 14" fill="none" stroke="#fff"/></svg>
      <span>www. ShoreLaneSmiles.com</span>
    </div>
  </div>
</section>

<section class="postcard postcard--back" aria-label="Postcard back">
  <svg class="card-art" viewBox="0 0 775 501" width="775" height="501">
    <defs>
      <clipPath id="leftPanel"><path d="M0 0 H374 Q470 110 459 248 Q450 400 334 501 H0 Z"/></clipPath>
    </defs>
    <path d="M384 0 Q484 110 472 250 Q462 410 346 501 H334 Q450 400 459 248 Q470 110 374 0 Z" fill="#1e8fcf"/>
    <g clip-path="url(#leftPanel)">
      <rect x="0" y="0" width="480" height="501" fill="#6b6c70"/>
      <path d="M0 0 H480 V220 Q300 180 160 195 Q60 205 0 230 Z" fill="#eedad6" role="img" aria-label="Photo of hands fitting a clear aligner onto teeth"/>
    </g>
  </svg>

  <div class="abs features">
    <div class="feature">
      <svg class="feature-icon" viewBox="0 0 36 36"><circle cx="18" cy="18" r="17" fill="#1e8fcf" stroke="#fff" stroke-width="1.5"/><path d="M18 9l7 3v5c0 5-3 8-7 10-4-2-7-5-7-10v-5z" fill="none" stroke="#fff" stroke-width="1.8"/><path d="M18 15v6M15 18h6" stroke="#fff" stroke-width="1.8"/></svg>
      <span>Major dental<br>insurance plans<br>and Cara-Plan<br>accepted</span>
    </div>
    <div class="feature">
      <svg class="feature-icon" viewBox="0 0 36 36"><circle cx="18" cy="18" r="17" fill="#1e8fcf" stroke="#fff" stroke-width="1.5"/><circle cx="18" cy="15" r="4" fill="none" stroke="#fff" stroke-width="1.8"/><path d="M9 24q4-3 9 0t9-2" fill="none" stroke="#fff" stroke-width="1.8"/></svg>
      <span>Affordable<br>payment<br>options are<br>available</span>
    </div>
    <div class="feature">
      <svg class="feature-icon" viewBox="0 0 36 36"><circle cx="18" cy="18" r="17" fill="#1e8fcf" stroke="#fff" stroke-width="1.5"/><path d="M12 10l3 3-1.5 1.5a8 8 0 0 0 4.5 4.5L19.5 17.5l3 3-2 2C15 22 10 17 10 12z" fill="#fff"/><circle cx="23" cy="12" r="3.5" fill="#fff"/></svg>
      <span>Call to schedule<br>your free<br>consultation</span>
    </div>
  </div>

  <div class="abs offer-box back-offer">
    <div class="offer-text"><span class="l1">PRESENT THIS NEW PATIENT</span><span class="l2">OFFER TO RECEIVE</span></div>
    <div class="offer-cta"><span>YOUR</span><span>DISCOUNT</span></div>
  </div>
  <p class="abs back-ends">OFFER ENDS<br>JANUARY 31</p>
  <div class="abs back-rule"></div>

  <div class="abs back-footer">
    <div class="row">
      <svg class="icon" style="width:11px;height:11px" viewBox="0 0 16 16"><path d="M4 1l3 3-1.6 1.6a9 9 0 0 0 5 5L12 9l3 3-2 2C7 14 2 9 2 3z" fill="#fff"/></svg>
      <span class="phone-num">805-472-9186</span>
    </div>
    <div class="row">
      <svg class="icon" style="width:11px;height:11px" viewBox="0 0 16 16"><circle cx="8" cy="8" r="7" fill="none" stroke="#fff" stroke-width="1.5"/></svg>
      <span>office@shorelanesmiles.com</span>
    </div>
    <div class="col2">
      <div class="row"><svg class="icon" style="width:10px;height:10px" viewBox="0 0 16 16"><path d="M8 1a5 5 0 0 1 5 5c0 4-5 9-5 9S3 10 3 6a5 5 0 0 1 5-5z" fill="#fff"/></svg><span>Harlow Street, Suite B, Ventura, CA 93001-2718</span></div>
      <div class="row"><svg class="icon" style="width:10px;height:10px" viewBox="0 0 16 16"><circle cx="8" cy="8" r="7" fill="none" stroke="#fff" stroke-width="1.5"/></svg><span>www. ShoreLaneSmiles.com</span></div>
    </div>
  </div>

  <div class="abs brand brand--back">
    <span class="brand-dot"></span><span class="brand-name">SHORE LANE SMILES</span>
  </div>
  <div class="abs stamp"></div>
  <div class="abs address-line" style="top:209px"></div>
  <div class="abs address-line" style="top:255px"></div>
  <div class="abs address-line" style="top:299px"></div>
</section>

</body>
</html>
```